New look while maintaining the Brand identification!

I want a new look for my business card. I want to keep the same colors and feel but change the look and layout a bit. The logo (KALMORETIX Physical therapy Reimagined and the lilypad) must remain the same and in that font.
We are a physical therapy clinic. So we have certification that we can write on the back or services we provide (which is what we currently have on the back of the card as well)

Contact information
2840 Cedar Hollow Rd., #22
Naples, FL 34276
P: (239) 555-0172
F: (239) 555-0198
E: kalmoretixcare@mailvexo.com
W: www.kalmoretixcare-example.com

Industry/Entity Type

Physical Therapy

Contact Information for Business Card

Our current cards have the business address and information on the back. But I am willing to have it be in the front.

Font styles to use
Sans Serif

Colors
abd036
fbf289
ec1f27

Requirements
Must have
• Has to be unique!
• Services we provide and/or techniques we do must fit on the card
Nice to have
• Would like to have the front and back somehow linked together. Such that if you set the front next to the back, there is a nice flow of design! Currently the back is white with writing on it.
Should not have
• I like the wave lines as compared to straight lines.

```html
<!DOCTYPE html>
<html lang="en">
<head>
<meta charset="utf-8">
<title>KALMORETIX Business Card</title>
<link rel="stylesheet" href="https://fonts.googleapis.com/css2?family=Lato:wght@400;700&family=Oswald:wght@500&display=swap">
<style>
  :root {
    --green: #abd036;
    --olive: #9aab2e;
    --olive-soft: #e3e9cc;
    --gold: #d6b32a;
    --text: #3d3d3d;
    --muted: #5a5a5a;
    --stage: #ececec;
    --paper: #ffffff;
  }
  * { margin: 0; padding: 0; box-sizing: border-box; }
  html, body { width: 1200px; height: 1000px; overflow: hidden; background: var(--paper); }
  .canvas { position: relative; width: 1200px; height: 1000px; }
  .stage { position: absolute; left: 0; top: 0; width: 1200px; height: 830px; background: var(--stage); }
  .card {
    position: absolute; top: 265px; width: 513px; height: 292px;
    background: var(--paper); overflow: hidden;
    font-family: "Lato", sans-serif; color: var(--text);
  }
  .card--front { left: 84px; }
  .card--back { left: 607px; }
  .card__mark-area { position: absolute; top: 10px; height: 216px; background: var(--olive-soft); border-radius: 40px; }
  .card--front .card__mark-area { left: 352px; width: 161px; border-top-right-radius: 0; border-bottom-right-radius: 0; }
  .card--back .card__mark-area { left: 0; width: 201px; border-top-left-radius: 0; border-bottom-left-radius: 0; }
  .card__wave { position: absolute; left: 0; top: 0; width: 513px; height: 292px; }
  .holder__name { position: absolute; left: 36px; top: 26px; font-size: 26px; font-weight: 400; color: var(--olive); }
  .holder__title { position: absolute; left: 36px; top: 58px; font-size: 11px; font-weight: 700; color: var(--muted); letter-spacing: 0.3px; }
  .address { position: absolute; left: 42px; top: 103px; font-size: 13px; line-height: 18px; color: var(--muted); letter-spacing: 0.3px; }
  .contacts { position: absolute; left: 38px; top: 147px; list-style: none; font-size: 13px; color: var(--text); }
  .contacts li { display: flex; align-items: center; height: 20px; }
  .contacts svg { width: 12px; height: 12px; margin-right: 11px; fill: var(--green); }
  .contacts .accent { color: var(--gold); }
  .brand { position: absolute; right: 52px; top: 150px; display: flex; flex-direction: column; align-items: center; }
  .brand__dot { width: 20px; height: 20px; border-radius: 50%; background: var(--olive); margin-bottom: 4px; }
  .brand__name { font-family: "Oswald", sans-serif; font-weight: 500; font-size: 28px; line-height: 30px; color: var(--gold); letter-spacing: 0.5px; }
  .brand__tagline { font-family: "Lato", sans-serif; font-size: 11px; font-weight: 700; color: var(--muted); margin-top: 2px; }
  .footer-brand {
    position: absolute; left: 0; top: 858px; width: 1200px;
    display: flex; flex-direction: column; align-items: center;
  }
  .footer-brand__dot { width: 40px; height: 40px; border-radius: 50%; background: var(--olive); margin-bottom: 6px; }
  .footer-brand__name {
    font-family: "Oswald", sans-serif; font-weight: 500; font-size: 64px; line-height: 70px;
    color: var(--gold); letter-spacing: 1px;
  }
</style>
</head>
<body>
<div class="canvas">
  <div class="stage"></div>

  <section class="card card--front">
    <div class="card__mark-area" role="img" aria-label="Large brand lily mark spanning both cards"></div>
    <svg class="card__wave" viewBox="0 0 513 292" aria-hidden="true">
      <path d="M0,238 C150,250 320,258 513,254 L513,292 L0,292 Z" fill="var(--green)"/>
      <path d="M0,227 C150,232 340,246 513,248" fill="none" stroke="var(--gold)" stroke-width="4"/>
    </svg>
    <h1 class="holder__name">Dana Merrow</h1>
    <p class="holder__title">PT, DPT, MSPT, MBA</p>
    <p class="address">2840 Cedar Hollow Rd., #22<br>Naples, FL 34276</p>
    <ul class="contacts">
      <li><svg viewBox="0 0 12 12"><path d="M1,4 C1,2 3,1 6,1 C9,1 11,2 11,4 L8,5 L8,3.5 L4,3.5 L4,5 Z M2,7 L4,5.5 L8,5.5 L10,7 L10,11 L2,11 Z"/></svg>(239) 555-0172</li>
      <li><svg viewBox="0 0 12 12"><path d="M3,1 H9 V5 H3 Z M1,5 H11 V10 H1 Z"/></svg>(239) 555-0198</li>
      <li><svg viewBox="0 0 12 12"><path d="M1,2.5 H11 V9.5 H1 Z" /><path d="M1,2.5 L6,6.5 L11,2.5" fill="none" stroke="#fff" stroke-width="1"/></svg>kalmoretixcare@mailvexo.com</li>
      <li><svg viewBox="0 0 12 12"><circle cx="7.5" cy="4.5" r="3.2" fill="none" stroke="var(--green)" stroke-width="1.6"/><path d="M5.2,6.8 L1.5,10.5" stroke="var(--green)" stroke-width="1.8"/></svg>www.<span class="accent">kalmoretixcare-example</span>.com</li>
    </ul>
  </section>

  <section class="card card--back">
    <div class="card__mark-area" role="img" aria-label="Large brand lily mark spanning both cards"></div>
    <svg class="card__wave" viewBox="0 0 513 292" aria-hidden="true">
      <path d="M0,252 C200,262 360,262 513,232 L513,292 L0,292 Z" fill="var(--green)"/>
      <path d="M0,242 C170,250 340,250 513,216" fill="none" stroke="var(--gold)" stroke-width="4"/>
    </svg>
    <div class="brand">
      <span class="brand__dot" aria-hidden="true"></span>
      <p class="brand__name">KALMORETIX</p>
      <p class="brand__tagline">Physical therapy Reimagined</p>
    </div>
  </section>

  <div class="footer-brand">
    <span class="footer-brand__dot" aria-hidden="true"></span>
    <p class="footer-brand__name">KALMORETIX</p>
  </div>
</div>
</body>
</html>
```